IT Network Consultancy - Business Card

kelbrin systems is a IT network consultancy based in London. We're looking for a smart, modern and professional business card design. Our website is here: www.kelbrinsystems.co.uk

Key things that should be included on the card (with examples):

Company Logo
Name
Position / Job Title: Network Consultant
Mobile Phone Number: +44 (0) 7700 900418
Land Line: +44 (0) 1632 960735
Email Address: name@kelbrinsystems.co.uk
Web Site URL: www.kelbrinsystems.co.uk

Target Market(s)

Large enterprise / global companies / corporates

Industry/Entity Type

Business

Requirements
Must have
• Incorporate our logo - which is attached to the project. They are in AI format (can be opened in Inkscape).

The design should be double sided and fit on a UK standard 85mm × 55mm card and be in a format that retains the quality when printed.
Nice to have
• The project does not have to conform to the colour of our website but this should give you inspiration of the style we like.
Should not have
• Bright colours. Pictures are not necessary.

```html
<!DOCTYPE html>
<html lang="en">
<head>
<meta charset="utf-8">
<title>kelbrin systems – Business Card</title>
<link rel="stylesheet" href="https://fonts.googleapis.com/css2?family=Josefin+Sans:wght@300;400;600&display=swap">
<style>
  :root {
    --page-bg: #8e8e8e;
    --card-bg: #ffffff;
    --panel-light: #8c8c8c;
    --panel-dark: #5b5b5b;
    --brand-text: #e4e8ec;
    --ink-dark: #3a3a3a;
    --ink-label: #2f2f2f;
    --ink-soft: #8d98a4;
  }
  * { margin: 0; padding: 0; box-sizing: border-box; }
  html, body {
    width: 1200px;
    height: 1200px;
    overflow: hidden;
    background: var(--page-bg);
    font-family: "Josefin Sans", "Century Gothic", sans-serif;
  }
  .card {
    position: absolute;
    left: 229px;
    width: 742px;
    height: 479px;
    background: var(--card-bg);
    overflow: hidden;
  }
  .card--front { top: 82px; }
  .card--back { top: 636px; }

  .brand-panel {
    position: absolute;
    width: 365px;
    height: 234px;
    background: radial-gradient(ellipse at 50% 40%, var(--panel-light) 0%, var(--panel-dark) 100%);
    display: flex;
    align-items: center;
    justify-content: center;
  }
  .card--front .brand-panel { left: 193px; top: 114px; }
  .card--back .brand-panel { left: 0; top: 115px; }

  .brand-name {
    color: var(--brand-text);
    font-weight: 300;
    font-size: 40px;
    letter-spacing: 1px;
    text-transform: uppercase;
    text-align: center;
    line-height: 1.15;
  }

  .contact {
    position: absolute;
    right: 36px;
    top: 122px;
    width: 300px;
    text-align: right;
  }
  .contact__name {
    font-variant: small-caps;
    font-weight: 400;
    font-size: 40px;
    color: var(--ink-dark);
    letter-spacing: 1px;
    line-height: 1;
    white-space: nowrap;
  }
  .contact__role {
    font-variant: small-caps;
    font-weight: 400;
    font-size: 23px;
    color: var(--ink-soft);
    letter-spacing: 1.5px;
    margin-top: 6px;
    white-space: nowrap;
  }
  .contact__list { margin-top: 10px; }
  .contact__label {
    font-weight: 600;
    font-size: 16px;
    color: var(--ink-label);
    letter-spacing: 1px;
    line-height: 20px;
  }
  .contact__value {
    font-weight: 300;
    font-size: 19px;
    color: var(--ink-soft);
    letter-spacing: 1.2px;
    line-height: 24px;
    white-space: nowrap;
  }

  .website {
    position: absolute;
    left: 0;
    right: 0;
    bottom: 10px;
    text-align: center;
    font-size: 21px;
    font-weight: 400;
    letter-spacing: 1.5px;
    color: var(--ink-dark);
  }
</style>
</head>
<body>
  <section class="card card--front" aria-label="Card front">
    <div class="brand-panel">
      <span class="brand-name">kelbrin<br>systems</span>
    </div>
  </section>

  <section class="card card--back" aria-label="Card back">
    <div class="brand-panel">
      <span class="brand-name">kelbrin<br>systems</span>
    </div>

    <div class="contact">
      <p class="contact__name">Daniel Hartley</p>
      <p class="contact__role">Network Consultant</p>
      <dl class="contact__list">
        <dt class="contact__label">phone</dt>
        <dd class="contact__value">+44 (0) 1632 960735</dd>
        <dt class="contact__label">mobile</dt>
        <dd class="contact__value">+44 (0) 7700 900418</dd>
        <dt class="contact__label">email</dt>
        <dd class="contact__value">dhartley@kelbrinsystems.co.uk</dd>
      </dl>
    </div>

    <p class="website">www.kelbrinsystems.co.uk</p>
  </section>
</body>
</html>
```